Business card design needed

I need a business card for my private practice. I would like to see the designs that use bright blue and white. I would like to see similar designs as to the card below:
http://blog.printvarno.com/2009/designing-a-business-card-with-pv-ks517-template.html
I would like to see the back of the card have room for appointment times. Thank you.

Industry/Entity Type
Business
Contact Information for Business Card
Brightwater Counselling & Wellness Services
Helen Dorsey B.Psychology
Registered Psychologist
Building C, Level 3, 14 Marrow Crescent, Canberra, ACT 2601
T: (02) 6287 5912
F: (02) 6287 5930
info@brightwatercounselling.com.au
www.brightwatercounselling.com.au

```html
<!DOCTYPE html>
<html lang="en">
<head>
<meta charset="utf-8">
<title>Brightwater Counselling &amp; Wellness Services — Business Card</title>
<link rel="stylesheet" href="https://fonts.googleapis.com/css2?family=Carlito:wght@400;700&display=swap">
<style>
  :root {
    --backdrop: #2b2b2d;
    --card: #f6f8fb;
    --brand-blue: #4a6891;
    --ink-blue: #2f4a70;
    --ink-grey: #4d5560;
  }
  html, body {
    margin: 0;
    padding: 0;
    width: 1200px;
    height: 942px;
    overflow: hidden;
    background: var(--backdrop);
  }
  .canvas {
    position: relative;
    width: 1200px;
    height: 942px;
  }
  .business-card {
    position: absolute;
    left: 100px;
    top: 185px;
    width: 1000px;
    height: 571px;
    background: var(--card);
    box-shadow: 0 14px 40px rgba(0,0,0,0.45);
    font-family: "Carlito", "Calibri", sans-serif;
    overflow: hidden;
  }
  .brand {
    position: absolute;
    left: 80px;
    top: 200px;
    display: flex;
    align-items: center;
    gap: 20px;
  }
  .brand-dot {
    width: 34px;
    height: 34px;
    border-radius: 50%;
    background: var(--brand-blue);
    flex: none;
  }
  .brand-name {
    margin: 0;
    font-size: 36px;
    font-weight: 700;
    line-height: 1.1;
    color: var(--ink-blue);
  }
  .contact-phones {
    position: absolute;
    right: 48px;
    top: 44px;
    margin: 0;
    font-size: 21px;
    color: var(--ink-grey);
  }
  .practitioner {
    position: absolute;
    left: 560px;
    top: 270px;
  }
  .practitioner-name {
    margin: 0;
    font-size: 40px;
    font-weight: 700;
    color: var(--ink-blue);
  }
  .practitioner-title {
    margin: 2px 0 0;
    font-size: 21px;
    color: var(--ink-grey);
  }
  .address {
    position: absolute;
    left: 470px;
    top: 385px;
    margin: 0;
    font-style: normal;
    font-size: 21px;
    line-height: 1.4;
    color: var(--ink-grey);
  }
</style>
</head>
<body>
<div class="canvas">
  <section class="business-card">
    <div class="brand">
      <span class="brand-dot"></span>
      <h1 class="brand-name">Brightwater Counselling &amp;<br>Wellness Services</h1>
    </div>

    <p class="contact-phones">T: (02) 6287 5912 &nbsp;F: (02) 6287 5930</p>

    <div class="practitioner">
      <h2 class="practitioner-name">Helen Dorsey</h2>
      <p class="practitioner-title">B.Psychology (Reg. Psychologist)</p>
    </div>

    <address class="address">
      Building C, Lvl 3, 14 Marrow Cres,<br>
      Canberra ACT 2601<br>
      info@brightwatercounselling.com.au<br>
      www.brightwatercounselling.com.au
    </address>
  </section>
</div>
</body>
</html>
```